Save The Date for 2019 RLX Colloquium

We have an annual meeting each June and need a Save the Date (STD) designed. It should be a two-sided postcard with room for address and stamp (according to US Mail postal standards). I have attached some examples from prior years, but we would appreciate a more modern and attractive design for this year's STD.

Target Market(s)

Our own members - nurses, nurse practitioners, PAs and physicians

Industry/Entity Type

Medical

Requirements
Must have
• Must include our logos (attached), ideally in a coordinating fashion - as was done in prior years (see examples attached) and without modifying the logos too much. Needs have the following information:
• - "Save the Date"
• - "The 12th Annual Heartline Crew Colloquium"
• - "Friday, June 7, 2019" or "6/7/19"
• - "The Varrick–Dunmore Building | 318 West 57th Street | NYC"
• - Please include our website (www.qb-zrh.org/events), phone number (212-555-0147) and email address (ask@qb-zrh.org) for people to ask questions
• - Must have space for a postage stamp and the name/address of the postcard recipient
Nice to have
• Would be nice to remain in our blue/grey/olive color palate (see attached Brand Standards guide).
Should not have
• Please do not use stock photos of medical staff. Please don't use cartoons or cartoon images (although a tasteful sketch may be considered).

```html
<!DOCTYPE html>
<html lang="en">
<head>
<meta charset="utf-8">
<title>Save the Date – 2019 RLX Colloquium</title>
<link href="https://fonts.googleapis.com/css2?family=Libre+Franklin:wght@300;400;700;800;900&family=Roboto+Condensed:ital,wght@0,400;1,400&display=swap" rel="stylesheet">
<style>
  :root {
    --backdrop: #c2bdb9;
    --navy: #0a3d78;
    --royal: #0587cf;
    --sky: #5aaee3;
    --sky-soft: #6fb2e3;
    --paper: #ffffff;
    --stamp: #d2d3d5;
    --rule: #c9cbce;
  }
  * { margin: 0; padding: 0; box-sizing: border-box; }
  html, body { width: 1200px; height: 1200px; overflow: hidden; }
  body {
    background: var(--backdrop);
    font-family: "Libre Franklin", Arial, sans-serif;
    color: var(--navy);
    position: relative;
  }
  .postcard {
    position: absolute;
    background: var(--paper);
    box-shadow: 2px 3px 5px rgba(0,0,0,0.25);
    overflow: hidden;
  }
  .postcard svg.art { position: absolute; inset: 0; }

  /* Front */
  .front { left: 264px; top: 95px; width: 674px; height: 475px; }
  .front .wash {
    position: absolute; inset: 0;
    background: linear-gradient(90deg, var(--paper) 33%, #a9cff0 65%, var(--sky) 100%);
  }
  .headline {
    position: absolute; left: 236px; top: 12px;
    font-weight: 900; font-size: 49px; letter-spacing: -0.3px; line-height: 1;
    white-space: nowrap;
    color: var(--sky);
  }
  .headline .strong { color: var(--navy); }
  .event-title { position: absolute; left: 237px; top: 98px; line-height: 1; white-space: nowrap; }
  .event-title .edition { font-weight: 300; font-size: 23px; display: block; margin-bottom: 8px; }
  .event-title .name-light { font-weight: 300; font-size: 43px; display: block; letter-spacing: 0.3px; }
  .event-title .name-bold { font-weight: 900; font-size: 43px; display: block; letter-spacing: 1px; margin-top: -3px; }
  .details { position: absolute; left: 237px; top: 222px; font-size: 17px; line-height: 25px; white-space: nowrap; }
  .details .date { font-weight: 800; font-size: 18px; }
  .contact { position: absolute; left: 237px; top: 310px; font-size: 17px; line-height: 19px; white-space: nowrap; }
  .contact .web { font-weight: 800; margin-bottom: 9px; display: block; }
  .contact b { font-weight: 700; }
  .partners {
    position: absolute; left: 14px; top: 402px; width: 650px; height: 60px;
    display: flex; align-items: center; justify-content: space-between;
    font-family: "Roboto Condensed", "Arial Narrow", sans-serif; font-size: 12.5px; line-height: 16px;
    white-space: nowrap;
  }
  .partner { display: flex; align-items: center; gap: 8px; }
  .partner .seal { width: 58px; height: 58px; border-radius: 50%; flex: none; }
  .seal.outline { border: 1.5px solid #8d96a3; background: var(--paper); }
  .seal.filled { background: var(--navy); }
  .seal.black { background: #111; width: 54px; height: 54px; }
  .partner em { font-style: italic; display: block; }

  /* Back */
  .back { left: 264px; top: 614px; width: 670px; height: 472px; }
  .org { position: absolute; left: 22px; top: 20px; display: flex; align-items: center; }
  .org .seal { width: 59px; height: 59px; border-radius: 50%; background: var(--navy); flex: none; }
  .org .org-rule { width: 1px; height: 42px; background: var(--navy); margin: 0 12px 0 12px; }
  .org .org-name { font-size: 22px; font-weight: 400; line-height: 1; white-space: nowrap; }
  .org .org-name small { display: block; font-size: 9px; letter-spacing: 0.5px; margin-top: 5px; }
  .return-address { position: absolute; left: 105px; top: 76px; font-size: 14.5px; line-height: 18.5px; white-space: nowrap; }
  .divider { position: absolute; left: 46px; top: 129px; width: 214px; height: 1px; background: var(--navy); }
  .message {
    position: absolute; left: 15px; top: 146px; width: 290px;
    font-size: 13.6px; line-height: 17.7px; text-align: justify; hyphens: auto;
  }
  .stamp { position: absolute; left: 557px; top: 14px; width: 98px; height: 110px; background: var(--stamp); }
  .address-line { position: absolute; left: 358px; width: 275px; height: 1px; background: var(--rule); }
</style>
</head>
<body>

<section class="postcard front">
  <div class="wash"></div>
  <svg class="art" width="674" height="475" viewBox="0 0 674 475">
    <defs>
      <linearGradient id="heartTone" x1="0" y1="0" x2="1" y2="1">
        <stop offset="0" stop-color="#1c5d9c"/>
        <stop offset="1" stop-color="#3f9ad6"/>
      </linearGradient>
    </defs>
    <path d="M0 0 H232 Q 206 312 0 392 Z" fill="var(--navy)"/>
    <path d="M0 0 H225 Q 197 298 0 378 Z" fill="var(--royal)"/>
    <rect x="0" y="0" width="180" height="245" rx="60" fill="url(#heartTone)" opacity="0.55"
          role="img" aria-label="Blue anatomical sketch of a human heart"/>
  </svg>

  <h1 class="headline">SAVE THE <span class="strong">DATE</span></h1>
  <h2 class="event-title">
    <span class="edition">THE 12TH ANNUAL</span>
    <span class="name-light">HEARTLINE CREW</span>
    <span class="name-bold">COLLOQUIUM</span>
  </h2>
  <div class="details">
    <div class="date">FRIDAY, JUNE 7, 2019</div>
    <div>The Varrick–Dunmore Building,</div>
    <div>318 West 57th Street, NYC</div>
  </div>
  <div class="contact">
    <span class="web">www.qb-zrh.org/events</span>
    For additonal information call <b>(212-555-0147)</b><br>
    or email <b>(ask@qb-zrh.org)</b>
  </div>

  <div class="partners">
    <div class="partner">
      <span class="seal outline"></span>
      <div><em>Presented by</em>The Hudson Valley<br>Heart Society, Inc.</div>
    </div>
    <div class="partner">
      <span class="seal filled"></span>
      <div><em>of the</em>The Empire Region Chapter;<br>Northeast Vascular College</div>
    </div>
    <div class="partner">
      <span class="seal black"></span>
      <div><em>in Association with</em>The Metro Cardiac Institute</div>
    </div>
  </div>
</section>

<section class="postcard back">
  <svg class="art" width="670" height="472" viewBox="0 0 670 472">
    <defs>
      <linearGradient id="panelWash" x1="0" y1="0" x2="1" y2="0">
        <stop offset="0.08" stop-color="#ffffff"/>
        <stop offset="0.6" stop-color="#b5d6f1"/>
        <stop offset="1" stop-color="var(--sky-soft)"/>
      </linearGradient>
    </defs>
    <path d="M0 0 H292 Q 348 230 283 472 H0 Z" fill="url(#panelWash)"/>
    <path d="M294 0 Q 352 230 286 472" fill="none" stroke="var(--sky)" stroke-width="5"/>
    <path d="M299 0 Q 357 230 292 472" fill="none" stroke="var(--navy)" stroke-width="6"/>
  </svg>

  <div class="org">
    <span class="seal"></span>
    <span class="org-rule"></span>
    <span class="org-name">Empire Region<small>CHAPTER</small></span>
  </div>
  <div class="return-address">742 Larkin Avenue, Suite 1410<br>New York, NY 10019</div>
  <div class="divider"></div>
  <p class="message">Ovitaquos minvern atesequidel min ratem aut aut ulparumqui autempo reptaquiat. Inctios et rehendae quuntium essimillaces qui at ernatem. Nequi ad explaut et aute rescipitiame in porem esto et quatur? Ximped molorem ut moloraero quam ipidus, et que ne velest laborepudam as re quas a quissequam exerum volorrum, qui dolore sera nimo beriatecae. Nam facipicimod utae sum, conestio. Et es sinverr orestem aut magnati vidunt od que et vent que accatem a same lania voluptatia doluptasita derum fuga. Nam re et mi, comnia sendusaepe porest, in rerionserum aut dis eatus, sanimus.</p>

  <div class="stamp" aria-label="Postage stamp area"></div>
  <div class="address-line" style="top:274px"></div>
  <div class="address-line" style="top:319px"></div>
  <div class="address-line" style="top:364px"></div>
  <div class="address-line" style="top:401px"></div>
</section>

</body>
</html>
```